Trifold Flyer Brochure for Coastal Ridge Pain Management

After having received all of your designs, they are way to similar to what we already have. Please, create new flyers based on your unique perspectives. That's opening up color schemes completely to your liking. I am looking for a contemporary modern sleek look. Please, try to keep it simple and clean.
Updates

Project Deadline Extended Reason: Hello Everyone, After reviewing everyone's Flyer Designs it's become apparent that all of our requests were at least somewhat met, but they all look very similar to our original design. That said, we are requesting completely different flyer designs. I'll submit the details here then list the changes in the overview as well. I'm requesting: Please, you chose your own color scheme and a sleek, crisp contemporary modern look. We're looking for your unique perspective into flyer design. We've extended the deadline to 7/6 and look forward to receiving your new and revised designs. Added Tuesday, July 4, 2017

Project Deadline Extended Reason: Hello all, I've just paid to extend an extra 5 days to make sure you have time to design. Thank you in advance for your re-submissions. Added Tuesday, July 4, 2017

Target Market(s)

Florida, U.S.A.

Industry/Entity Type

Health And Wellness

Logo Text

CRPM

Requirements
Must have
• Color of your choice, contemporary modern, sleek and clean look.
Should not have
• Remove Dr. Neil Barstowe from the back of the brochure

```html
<!DOCTYPE html>
<html lang="en">
<head>
<meta charset="utf-8">
<title>Coastal Ridge Pain Management – Trifold Brochure</title>
<link href="https://fonts.googleapis.com/css2?family=Lato:ital,wght@0,400;0,700;1,400;1,700&family=Montserrat:wght@300;800&family=Oswald:wght@700&display=swap" rel="stylesheet">
<style>
  :root{
    --blue:#0d55a6;
    --blue-deep:#0a4a96;
    --teal:#17a895;
    --green:#1fc49a;
    --ink:#333a44;
    --paper:#ffffff;
    --paper-grey:#e9eaec;
    --stage:#d9dadc;
  }
  *{box-sizing:border-box;margin:0;padding:0}
  html,body{width:1200px;height:1200px;overflow:hidden;background:var(--stage)}
  body{font-family:"Lato",sans-serif;color:var(--ink);position:relative}
  .brochure{position:absolute;left:0;top:135px;width:1200px;height:930px;display:flex;box-shadow:0 10px 30px rgba(0,0,0,.2)}
  .panel{position:relative;width:400px;height:930px;overflow:hidden}
  .panel-art{position:absolute;inset:0;width:100%;height:100%}

  /* left panel */
  .about{background:var(--paper)}
  .about .content{position:absolute;left:48px;top:60px;width:310px}
  .about .lower{position:absolute;left:48px;top:640px;width:310px}
  .heading{font-style:italic;font-weight:700;color:var(--teal);font-size:13px;margin-bottom:6px;letter-spacing:.3px}
  .body-copy{font-style:italic;font-size:10.5px;line-height:1.45;margin-bottom:14px}
  .provider{margin-bottom:18px}
  .provider-name{font-style:italic;font-weight:700;color:var(--teal);font-size:13px;line-height:1.25;margin-bottom:4px}
  .provider-creds{font-style:italic;font-size:10px;line-height:1.4}

  /* middle panel */
  .locations{background:var(--paper)}
  .location{position:absolute;left:60px;width:280px}
  .map{width:280px;height:150px;background:#f4f6f8;border:3px solid #2a2d33}
  .address{margin-top:14px;background:var(--paper);box-shadow:0 2px 6px rgba(0,0,0,.15);padding:8px 12px;font-size:10.5px;line-height:1.4}

  /* cover panel */
  .cover{background:var(--paper)}
  .brand{position:absolute;left:70px;top:70px;display:flex;align-items:center;gap:12px}
  .brand-mark{width:40px;height:40px;background:var(--blue)}
  .brand-name{font-family:"Lato",sans-serif;font-weight:700;color:var(--blue);font-size:17px;line-height:1.2;width:200px}
  .cover-photo{position:absolute;left:0;top:190px;width:400px;height:560px;background:linear-gradient(160deg,#6fa04a 0%,#9cc36a 35%,#d8d2c4 75%,#c9c3b4 100%)}
  .tagline{position:absolute;left:0;right:0;top:740px;text-align:center;color:#fff}
  .tag-1{font-family:"Montserrat",sans-serif;font-weight:800;font-size:28px;letter-spacing:2px}
  .tag-2{font-family:"Montserrat",sans-serif;font-weight:300;font-size:25px;letter-spacing:1px;margin-top:2px}
  .tag-3{font-family:"Oswald",sans-serif;font-weight:700;font-size:42px;color:var(--green);letter-spacing:1px;margin-top:2px;line-height:1.1}
  .url{display:inline-block;margin-top:18px;background:#fff;color:var(--blue);border-radius:20px;padding:8px 34px;font-weight:700;font-size:14px;letter-spacing:4px}
</style>
</head>
<body>
<main class="brochure">

  <section class="panel about">
    <svg class="panel-art" viewBox="0 0 400 930" aria-hidden="true">
      <rect width="400" height="10" fill="var(--blue)"/>
      <polygon points="0,600 400,600 400,930 0,930" fill="var(--paper-grey)"/>
      <polygon points="0,545 400,625 400,650 0,575" fill="var(--blue)"/>
    </svg>
    <div class="content">
      <h2 class="heading">ABOUT US</h2>
      <p class="body-copy">We are one of the largest comprehensive pain management groups in the Tampa Bay area with offices located in Pinellas, Pasco and Hernando Counties. Utilizing the latest diagnostic and therapeutic technology, our goal is to identify, reduce or eliminate pain and help to avoid major surgical procedures.</p>
      <h2 class="heading">OUR PROVIDERS</h2>
      <p class="body-copy">Lorem Ipsum is simply dummy text of the printing and typesetting industry. Lorem Ipsum has been the industry's standard dummy text ever since the 1500s, when an unknown</p>
      <div class="provider">
        <h3 class="provider-name">Omar Valdane,<br>MD Medical Director</h3>
        <p class="provider-creds">Board Certified in Anesthesiology<br>Board Certified in Pain Management<br>Diplomate National Academy of Pain Care<br>Fellowship Trained Pain Management Specialist</p>
      </div>
      <div class="provider">
        <h3 class="provider-name">Leena Marcott, MD</h3>
        <p class="provider-creds">Fellowship Trained Pain Management Specialist<br>Diplomate National Academy of Pain Care<br>Fellow of Westbridge College of Surgery</p>
      </div>
    </div>
    <div class="lower">
      <div class="provider">
        <h3 class="provider-name">Grant Ellory, MD</h3>
        <p class="provider-creds">Board Certified in Anesthesiology<br>Board Certified in Pain Management<br>Fellowship Trained Pain Management Specialist</p>
      </div>
      <div class="provider">
        <h3 class="provider-name">Peter Haldwin, MD</h3>
        <p class="provider-creds">Board Eligible in Anesthesiology<br>Board Eligible in Pain Management<br>Fellowship Trained Pain Management Specialist</p>
      </div>
      <div class="provider">
        <h3 class="provider-name">Russell Brandt, Psy-D</h3>
        <p class="provider-creds">Licensed Psychologist<br>Specialize in Chronic Pain/ Bio Feedback</p>
      </div>
    </div>
  </section>

  <section class="panel locations">
    <svg class="panel-art" viewBox="0 0 400 930" aria-hidden="true">
      <path d="M0,0 H400 V28 Q200,-10 0,28 Z" fill="var(--teal)"/>
      <polygon points="0,900 400,880 400,890 0,910" fill="var(--blue)"/>
    </svg>
    <div class="location" style="top:70px">
      <div class="map" role="img" aria-label="Street map showing the first office location"></div>
      <p class="address">Office: (727) 555-0142 | Fax: (727) 555-0187<br>2710 Harbor Crest Ave. N. | Bayview,FL 33790</p>
    </div>
    <div class="location" style="top:350px">
      <div class="map" role="img" aria-label="Street map showing the second office location"></div>
      <p class="address">Office: (727) 555-0142 | Fax: (727) 555-0187<br>2710 Harbor Crest Ave. N. | Bayview,FL 33790</p>
    </div>
    <div class="location" style="top:630px">
      <div class="map" role="img" aria-label="Street map showing the third office location"></div>
      <p class="address">Office: (727) 555-0142 | Fax: (727) 555-0187<br>2710 Harbor Crest Ave. N. | Bayview,FL 33790</p>
    </div>
  </section>

  <section class="panel cover">
    <svg class="panel-art" viewBox="0 0 400 930" aria-hidden="true">
      <rect width="400" height="10" fill="var(--blue)"/>
    </svg>
    <div class="brand">
      <span class="brand-mark"></span>
      <span class="brand-name">Coastal Ridge Pain Management</span>
    </div>
    <div class="cover-photo" role="img" aria-label="Photo of a woman and a man jogging together on a sunny park path"></div>
    <svg class="panel-art" viewBox="0 0 400 930" aria-hidden="true">
      <polygon points="0,640 190,560 400,720 400,930 0,930" fill="var(--blue-deep)"/>
    </svg>
    <div class="tagline">
      <div class="tag-1">OUR GOAL IS</div>
      <div class="tag-2">TO GET YOU BACK</div>
      <div class="tag-3">TO LIVING AGAIN</div>
      <div class="url">www.crpm-care.com</div>
    </div>
  </section>

</main>
</body>
</html>
```